Design a Professional Business Card for Velmora Arcs

Design a business card for Velmora Arcs, we are a National Sport Court Company.

West Region Address: 4175 Quill Harbor Ln, Suite #215 Englewood, Colorado 80467
East Region Address: 3817 Tamsin Rd E, Bradenton, Florida 34583

Target Market(s)

High End Residential & Institutional Clients

Industry/Entity Type

Design & Construction

Contact Information for Business Card

Logo/Brand/Colors/ name, number (provided in comments)

Requirements
Must have
• Colors only provided in logo
Should not have
• Any other colors not in existing logo (attached)

```html
<!DOCTYPE html>
<html lang="en">
<head>
<meta charset="utf-8">
<title>Velmora Arcs — Business Card</title>
<link href="https://fonts.googleapis.com/css2?family=Poppins:wght@400;500;600;700&display=swap" rel="stylesheet">
<style>
  :root {
    --navy: #1f3566;
    --green: #1b6d3b;
    --ink: #3a3f47;
    --card: #ffffff;
    --backdrop: #e6e7e9;
    --faint: #eef0f2;
  }
  * { box-sizing: border-box; margin: 0; padding: 0; }
  html, body { width: 1200px; height: 900px; overflow: hidden; }
  body {
    background: var(--backdrop);
    font-family: "Poppins", sans-serif;
    display: flex; flex-direction: column; align-items: center; justify-content: center;
    gap: 44px;
  }
  .card {
    position: relative;
    width: 630px; height: 360px;
    background: var(--card);
    box-shadow: 0 6px 22px rgba(0,0,0,.12);
    overflow: hidden;
  }
  .brand { display: flex; align-items: center; gap: 16px; }
  .brand-dot { width: 62px; height: 62px; border-radius: 50%; background: var(--navy); flex: none; }
  .brand-name {
    font-weight: 700; color: var(--navy); font-size: 34px; line-height: 1;
    letter-spacing: 2px; text-transform: uppercase;
  }

  /* front */
  .card-front .brand { position: absolute; left: 50%; top: 118px; transform: translateX(-50%); }
  .card-front .site {
    position: absolute; left: 0; right: 0; bottom: 56px; text-align: center;
    font-size: 15px; font-weight: 600; letter-spacing: 4px; color: var(--navy);
  }
  .card-front .site .domain { color: var(--green); }

  /* back */
  .backdrop-circle {
    position: absolute; left: -20px; top: 130px; width: 290px; height: 290px;
    border-radius: 50%; background: var(--faint);
  }
  .card-back .brand { position: absolute; right: 48px; top: 40px; }
  .card-back .brand-dot { width: 54px; height: 54px; }
  .card-back .brand-name { font-size: 30px; }
  .divider {
    position: absolute; left: 232px; right: 0; top: 178px;
    height: 1.5px; background: var(--green);
  }
  .person { position: absolute; left: 40px; top: 156px; }
  .person-name { font-size: 16px; font-weight: 600; color: var(--navy); text-transform: uppercase; letter-spacing: .3px; }
  .person-role { font-size: 14px; color: var(--green); margin-top: 4px; }
  .contacts { position: absolute; left: 40px; bottom: 30px; list-style: none; }
  .contacts li {
    display: flex; align-items: center; gap: 10px;
    font-size: 13.5px; color: var(--ink); line-height: 25px;
  }
  .contacts svg { width: 14px; height: 14px; flex: none; }
  .offices { position: absolute; right: 40px; top: 200px; text-align: right; }
  .office { font-size: 13.5px; color: var(--ink); line-height: 21px; margin-bottom: 16px; }
  .office .region { color: var(--navy); font-weight: 500; }
</style>
</head>
<body>

  <section class="card card-front">
    <div class="brand">
      <span class="brand-dot"></span>
      <span class="brand-name">Velmora Arcs</span>
    </div>
    <p class="site">www.<span class="domain">velmoraarcs</span>.com</p>
  </section>

  <section class="card card-back">
    <div class="backdrop-circle"></div>
    <div class="brand">
      <span class="brand-dot"></span>
      <span class="brand-name">Velmora Arcs</span>
    </div>
    <div class="divider"></div>

    <div class="person">
      <p class="person-name">Dorian M. Kessler, ASLA</p>
      <p class="person-role">CEO &amp; Founder</p>
    </div>

    <div class="offices">
      <p class="office"><span class="region">East Region</span> - 3817 Tamsin Rd E<br>Bradenton, Florida 34583</p>
      <p class="office"><span class="region">West Region</span> - 4175 Quill Harbor Ln<br>Suite #215 Englewood, Colorado 80467</p>
    </div>

    <ul class="contacts">
      <li><svg viewBox="0 0 14 14"><rect x="3.5" y="1" width="7" height="12" rx="1.5" fill="none" stroke="var(--navy)" stroke-width="1.3"/></svg>(303) 555-0147</li>
      <li><svg viewBox="0 0 14 14"><path d="M3 1.5l2.2 2.6-1.3 1.6a8 8 0 0 0 4.4 4.4l1.6-1.3 2.6 2.2-1.4 1.6C6 12.4 1.6 8 1.4 2.9z" fill="var(--navy)"/></svg>1-800-555-0193</li>
      <li><svg viewBox="0 0 14 14"><rect x="1" y="3" width="12" height="8.5" fill="var(--navy)"/><path d="M1 3l6 5 6-5" fill="none" stroke="#fff" stroke-width="1"/></svg>dorian@velmoraarcs.com</li>
      <li><svg viewBox="0 0 14 14"><g fill="none" stroke="var(--navy)" stroke-width="1"><circle cx="7" cy="7" r="5.8"/><ellipse cx="7" cy="7" rx="2.6" ry="5.8"/><path d="M1.2 7h11.6M2 4h10M2 10h10"/></g></svg>www.velmoraarcs.com</li>
    </ul>
  </section>

</body>
</html>
```